Building Company Business Card Design

Need a design for a business card:
It needs to have: Name, Phone, Facebook link, Website, email
i would also like a list of works we undertake:
-New Homes
-Extensions, Renovations & Bathrooms
-Decking, Carports, Sheds (Residential and Industrial)
-Carpentry
-Fences, Patios & Pergolas

Contact Information for Business Card

Name, Phone, Facebook link, Website, email + details of services provided listed in description

```html
<!DOCTYPE html>
<html lang="en">
<head>
<meta charset="utf-8">
<title>Ridgeline Homes – Business Card</title>
<link href="https://fonts.googleapis.com/css2?family=Arimo:wght@400;700&display=swap" rel="stylesheet">
<style>
  :root {
    --page: #e9e9e9;
    --green: #33b44f;
    --black: #0d0d0d;
    --black-soft: #1a1a1a;
    --rim: #8a8a8a;
    --white: #ffffff;
    --grey-text: #bdbdbd;
  }
  * { margin: 0; padding: 0; box-sizing: border-box; }
  html, body { width: 1200px; height: 802px; overflow: hidden; background: var(--page); }
  body { font-family: "Arimo", Arial, sans-serif; position: relative; }

  .card {
    position: absolute; top: 246px; width: 540px; height: 309px;
    overflow: hidden; box-shadow: 0 6px 18px rgba(0,0,0,.25);
  }
  .card--front { left: 40px; background: var(--green); }
  .card--back { left: 620px; background: linear-gradient(160deg, var(--black-soft), var(--black) 60%); }

  .front-shape { position: absolute; inset: 0; }

  .brand { position: absolute; color: var(--white); text-transform: uppercase; font-weight: 700; }
  .brand__name { font-size: 30px; letter-spacing: 1px; line-height: 1; }
  .brand__sub { font-size: 11.5px; letter-spacing: 1px; margin-top: 4px; color: var(--grey-text); }
  .card--front .brand { left: 292px; top: 92px; }
  .card--back .brand { left: 30px; bottom: 30px; }

  .contact { position: absolute; left: 30px; top: 150px; color: var(--white); width: 240px; }
  .contact__name { font-size: 19px; font-weight: 700; letter-spacing: 1px; text-transform: uppercase; }
  .contact__role { font-size: 13px; margin-top: 2px; }
  .contact__rule { border: 0; border-top: 1px solid var(--white); margin: 10px 0 9px; width: 210px; }
  .contact__list { list-style: none; font-size: 13px; line-height: 19px; }
  .contact__list li { display: flex; align-items: center; gap: 8px; }
  .contact__list svg { width: 12px; height: 12px; flex: none; }

  .services { position: absolute; left: 30px; top: 38px; list-style: none; color: var(--white); font-size: 16px; line-height: 23px; }
  .services li::before { content: "\2022"; color: var(--grey-text); margin-right: 6px; }
</style>
</head>
<body>

<section class="card card--front">
  <svg class="front-shape" viewBox="0 0 540 309" aria-hidden="true">
    <circle cx="410" cy="30" r="262" fill="var(--rim)"/>
    <circle cx="418" cy="24" r="258" fill="var(--black)"/>
  </svg>
  <div class="brand">
    <div class="brand__name">Ridgeline Homes</div>
    <div class="brand__sub">and Developments Pty Ltd</div>
  </div>
  <div class="contact">
    <div class="contact__name">Marcus Dale</div>
    <div class="contact__role">Manager</div>
    <hr class="contact__rule">
    <ul class="contact__list">
      <li><svg viewBox="0 0 12 12"><path d="M3 1l2 2-1 1.5c.7 1.5 1.8 2.6 3.5 3.5L9 7l2 2-1.5 2C5 10.5 1.5 7 1 2.5z" fill="#fff"/></svg>555-018-4420</li>
      <li><svg viewBox="0 0 12 12"><rect x="1" y="2.5" width="10" height="7" fill="none" stroke="#fff"/><path d="M1 2.5l5 4 5-4" fill="none" stroke="#fff"/></svg>marcus@ridgelinemail.com</li>
      <li><svg viewBox="0 0 12 12"><circle cx="6" cy="6" r="5" fill="none" stroke="#fff"/><path d="M1 6h10M6 1v10" stroke="#fff"/></svg>www.ridgelinehomes.example</li>
      <li><svg viewBox="0 0 12 12"><rect x="1" y="1" width="10" height="10" rx="2" fill="#fff"/></svg>#Ridgeline Homes</li>
    </ul>
  </div>
</section>

<section class="card card--back">
  <ul class="services">
    <li>Extensions, Renovations &amp; Bathrooms</li>
    <li>Decking, Carports, Sheds (Residential and Industrial)</li>
    <li>Carpentry</li>
    <li>Fences, Patios &amp; Pergolas</li>
  </ul>
  <div class="brand">
    <div class="brand__name">Ridgeline Homes</div>
    <div class="brand__sub">and Developments Pty Ltd</div>
  </div>
</section>

</body>
</html>
```